Plumweave Inc. Website & Korvix Apps Landing Pages

We need a web site design for our company. We develop software and do various consultant projects for our clients. Our products focus on the mobile platform, mainly the Korvix (business, games, social, etc.). We want to communicate that our software is simple and good as candy. The web pages should be fun to look at not loosing seriousness and credibility. Web 2.0 style and 960 grid system a must. We are opened to any overall site colour scheme suggestions (look at the sites we like below).

Must haves:
- Our logo should be seen on the site and look great on it :-) (preview attached below)
- Main home page and app landing page.
- Section links/tabs on the home page (home,apps,support,blog,contact,about)
- No text in images
- Style sheet

Looks we like:
- http://x7k3lmq9pwrtzv.pixelmoorvault.net/412_Zelto_Site/final_large.jpg
- http://x7k3lmq9pwrtzv.pixelmoorvault.net/Premium_71_Illustrative_Korvix_Landing_Page/final.jpg
- http://grelmwick.com/
- http://dorniply.ca/
- http://quatzel.com/

Industry/Entity Type

Business

Requirements
Must have
• - Company logo should look great on pages.
• - Main home page and app landing page.
• - Section links/tabs on the home page (home,apps,support,blog,contact,about)
• - Web 2.0 style.
• - 960 grid system (12 col, 16 col).
• - Sliced ann optmized
• - Exported in all major formats (psd,ai,eps,png,jpeg,etc)
• - Style sheet
Should not have
• - Text in images

```html
<!DOCTYPE html>
<html lang="en">
<head>
<meta charset="utf-8">
<title>App Name – Plumweave</title>
<link href="https://fonts.googleapis.com/css2?family=Arimo:wght@400;700&display=swap" rel="stylesheet">
<style>
  :root {
    --ink: #333333;
    --ink-soft: #5a5a5a;
    --heading-grey: #6a6a6a;
    --panel: #383838;
    --panel-edge: #1f1f1f;
    --brand-red: #d01f2c;
    --button-red-top: #c8202c;
    --button-red-bottom: #7d0a12;
    --footer: #3a3a3c;
    --footer-line: #1c1c1c;
    --footer-text: #e2e2e2;
    --paper: #ffffff;
  }
  * { box-sizing: border-box; margin: 0; padding: 0; }
  html, body { width: 1200px; height: 1170px; overflow: hidden; background: var(--paper); }
  body { position: relative; font-family: "Arimo", Arial, sans-serif; color: var(--ink); }
  .abs { position: absolute; }

  /* Header */
  .app-title { left: 132px; top: 26px; font-size: 52px; letter-spacing: -2.5px; color: var(--ink); font-weight: 400; }
  .byline { left: 382px; top: 50px; font-size: 11px; color: #555; }
  .brand-word { color: var(--brand-red); font-weight: 700; }
  .byline-brand { left: 472px; top: 42px; font-size: 24px; }
  .more-apps { right: 130px; top: 50px; font-size: 11px; color: #555; display: flex; align-items: center; gap: 4px; }
  .dot { display: inline-block; width: 12px; height: 12px; border-radius: 50%; background: var(--brand-red); }

  /* Hero */
  .hero-panel { left: 130px; top: 190px; width: 940px; height: 310px; background: var(--panel); border-radius: 6px; box-shadow: inset 0 0 0 2px var(--panel-edge); }
  .tagline { left: 191px; top: 232px; font-size: 50px; line-height: 50px; color: #fff; letter-spacing: -2.5px; font-weight: 400; }
  .hero-copy { left: 190px; top: 361px; width: 360px; font-size: 16px; line-height: 20px; color: #fff; }
  .cta { left: 189px; top: 461px; width: 236px; height: 62px; border-radius: 7px; background: linear-gradient(var(--button-red-top), var(--button-red-bottom)); border: 2px solid #e9e9e9; box-shadow: 0 2px 4px rgba(0,0,0,.35); color: #fff; font-size: 23px; letter-spacing: -0.8px; display: flex; align-items: center; justify-content: center; gap: 12px; }
  .cta .dot { width: 10px; height: 10px; background: #f2c7c9; }
  .device { left: 675px; top: 140px; width: 335px; height: 360px; border-radius: 44px 44px 0 0; background: linear-gradient(160deg, #e8e8e8 0%, #1a1a1a 6%, #0c0c0c 100%); }
  .device-screen { left: 698px; top: 257px; width: 289px; height: 243px; background: linear-gradient(#6fa6b3, #9cc3cc); }
  .store-badge { left: 849px; top: 472px; width: 163px; height: 59px; border-radius: 6px; background: linear-gradient(#b5161f, #6e0a10); border: 1px solid #e0e0e0; }

  /* Content */
  .section-title { top: 601px; font-size: 22px; color: var(--heading-grey); letter-spacing: -0.6px; font-weight: 700; }
  .overview-title { left: 194px; }
  .shots-title { left: 669px; }
  .features-title { left: 889px; }
  .overview { left: 192px; top: 648px; width: 395px; font-size: 14px; line-height: 20px; color: var(--ink-soft); letter-spacing: 0.4px; }
  .overview p + p { margin-top: 20px; }
  .shot { left: 670px; width: 160px; height: 109px; background: linear-gradient(90deg, #111 0 12px, #7fb0bb 12px 148px, #111 148px); border: 1px solid #222; }
  .shot-one { top: 651px; }
  .shot-two { top: 784px; }
  .features { left: 876px; top: 648px; list-style: none; font-size: 14px; line-height: 20px; color: #222; letter-spacing: 0.3px; }
  .features li { position: relative; padding-left: 13px; }
  .features li::before { content: ""; position: absolute; left: 1px; top: 7px; width: 6px; height: 6px; border-radius: 50%; background: #222; }
  .contact-button { left: 882px; top: 788px; width: 161px; height: 43px; border-radius: 6px; background: linear-gradient(#8a8a8a, #3d3d3d); border: 1px solid #222; box-shadow: inset 0 1px 0 #b0b0b0; color: #fff; font-size: 13px; display: flex; align-items: center; justify-content: center; }

  /* Footer */
  .site-footer { left: 0; top: 998px; width: 1200px; height: 172px; background: var(--footer); border-top: 3px solid var(--footer-line); }
  .copyright { left: 136px; top: 1030px; font-size: 11px; color: #cfcfcf; }
  .footer-brand { left: 135px; top: 1050px; font-size: 40px; letter-spacing: -0.5px; }
  .footer-nav { top: 1066px; left: 0; width: 1200px; height: 20px; list-style: none; }
  .footer-nav li { position: absolute; font-size: 15px; color: var(--footer-text); text-shadow: 0 1px 1px #000; display: flex; align-items: center; gap: 6px; }
  .footer-nav .dot { width: 12px; height: 12px; }
</style>
</head>
<body>
  <header>
    <h1 class="abs app-title">App Name</h1>
    <div class="abs byline">brought to you by</div>
    <div class="abs byline-brand brand-word">Plumweave</div>
    <div class="abs more-apps">See more Apps <span class="dot"></span></div>
  </header>

  <section class="hero">
    <div class="abs hero-panel"></div>
    <h2 class="abs tagline">This is a nice<br>and short tagline.</h2>
    <p class="abs hero-copy">And this is some dummy text: but as the junior mates were hurrying to execute the order, a pale man, with a bandaged head, arrested them.</p>
    <div class="abs cta"><span class="dot"></span>Call to Action<span class="dot"></span></div>
    <div class="abs device" role="img" aria-label="Photo of a Korvix phone showing its home screen"></div>
    <div class="abs device-screen" role="img" aria-label="Phone home screen with app icons"></div>
    <div class="abs store-badge" role="img" aria-label="App listing badge"></div>
  </section>

  <main>
    <h3 class="abs section-title overview-title">Overview</h3>
    <div class="abs overview">
      <p>This is some dummy text: beyond the DUODECIMO, this system does not proceed, inasmuch as the Porpoise is the smallest of the whales. Above, you have all the Leviathans of note.</p>
      <p>The end!&nbsp; The great and terrible day of the Lord!&nbsp; When men shall call upon the mountains and the rocks to fall upon them and hide them--hide them from the face of Him that sitteth upon the throne!"</p>
      <p>I began to understand the position.&nbsp; I ceased my laboured reasoning.</p>
    </div>

    <h3 class="abs section-title shots-title">Screenshots</h3>
    <div class="abs shot shot-one" role="img" aria-label="App screenshot on a Korvix phone"></div>
    <div class="abs shot shot-two" role="img" aria-label="App screenshot on a Korvix phone"></div>

    <h3 class="abs section-title features-title">Features</h3>
    <ul class="abs features">
      <li>And this is some dummy text</li>
      <li>But as the junior mates</li>
      <li>Were hurrying to execute</li>
      <li>A pale man</li>
      <li>With a bandaged head</li>
    </ul>
    <div class="abs contact-button">Contact us for more info</div>
  </main>

  <footer>
    <div class="abs site-footer"></div>
    <div class="abs copyright">©2010 Plumweave. All Rights Reserved.</div>
    <div class="abs footer-brand brand-word">Plumweave</div>
    <ul class="abs footer-nav">
      <li style="left:521px">Home</li>
      <li style="left:606px"><span class="dot"></span>Apps</li>
      <li style="left:706px">Support</li>
      <li style="left:814px">Blog</li>
      <li style="left:896px">Contact</li>
      <li style="left:1003px">About</li>
    </ul>
  </footer>
</body>
</html>
```